Business Card for a Renewable energy construction company

I need a formal, neat looking business card. Minimal and professional looking. Back side can have a design that is semi-ransparent/shaded

Target Market(s)

Renewable energy companies

Contact Information for Business Card

Name, Surname and contact details (phone, email)

Colors
00AB8E
00BBA5
67D7C9
C6EFE9
E9F9F6

Requirements
Must have
• Place for a QR code in the back side

```html
<!DOCTYPE html>
<html lang="en">
<head>
<meta charset="utf-8">
<title>Business Card – Front and Back</title>
<link rel="stylesheet" href="https://fonts.googleapis.com/css2?family=Ubuntu:wght@300;400;500&display=swap">
<style>
  :root {
    --page-bg: #dcd6cd;
    --card-white: #ffffff;
    --brand-teal: #02898f;
    --brand-teal-deep: #017f85;
    --brand-teal-light: #0a979c;
    --text-dark: #2f3236;
  }
  * { box-sizing: border-box; margin: 0; padding: 0; }
  html, body {
    width: 1200px;
    height: 1200px;
    overflow: hidden;
    background: var(--page-bg);
    font-family: "Ubuntu", sans-serif;
  }
  .sheet {
    width: 1200px;
    height: 1200px;
    display: flex;
    flex-direction: column;
    align-items: center;
    justify-content: center;
    gap: 60px;
  }
  .card {
    position: relative;
    width: 900px;
    height: 500px;
    overflow: hidden;
  }

  /* Front */
  .card-front { background: var(--card-white); }
  .accent-bar-top {
    position: absolute;
    left: 24px;
    top: 0;
    width: 32px;
    height: 175px;
    background: var(--brand-teal);
    border-radius: 0 0 10px 10px;
  }
  .identity {
    position: absolute;
    left: 80px;
    top: 46px;
    color: var(--brand-teal);
  }
  .identity-name {
    font-size: 42px;
    font-weight: 400;
    letter-spacing: 0.3px;
    line-height: 1.1;
  }
  .identity-position {
    font-size: 30px;
    font-weight: 300;
    margin-top: 4px;
    line-height: 1.1;
  }
  .contact-list {
    position: absolute;
    left: 24px;
    top: 360px;
    list-style: none;
    color: var(--text-dark);
  }
  .contact-item {
    display: flex;
    align-items: center;
    gap: 22px;
    font-size: 29px;
    font-weight: 300;
    height: 58px;
  }
  .contact-icon { width: 30px; height: 30px; flex: none; }
  .accent-bar-bottom {
    position: absolute;
    left: 548px;
    top: 280px;
    width: 32px;
    height: 220px;
    background: var(--brand-teal);
    border-radius: 10px 0 0 0;
  }
  .brand-name {
    position: absolute;
    left: 604px;
    top: 400px;
    width: 276px;
    text-align: center;
    font-size: 52px;
    font-weight: 500;
    letter-spacing: 2px;
    color: var(--brand-teal);
  }

  /* Back */
  .card-back { background: var(--brand-teal); }
  .turbine-pattern {
    position: absolute;
    inset: 0;
    background: linear-gradient(135deg, var(--brand-teal-light) 0%, var(--brand-teal-deep) 100%);
  }
  .qr-placeholder {
    position: absolute;
    left: 377px;
    top: 178px;
    width: 146px;
    height: 146px;
    border: 2px solid var(--card-white);
    display: flex;
    align-items: center;
    justify-content: center;
    color: var(--card-white);
    font-size: 48px;
    font-weight: 300;
  }
</style>
</head>
<body>
<main class="sheet">
  <section class="card card-front" aria-label="Business card front">
    <div class="accent-bar-top"></div>
    <div class="identity">
      <p class="identity-name">YOUR NAME &amp; SURNAME</p>
      <p class="identity-position">YOUR POSITION</p>
    </div>
    <ul class="contact-list">
      <li class="contact-item">
        <svg class="contact-icon" viewBox="0 0 24 24" aria-hidden="true">
          <path d="M6.6 3.5l2.6 3.2-1.6 2.1a11 11 0 0 0 7.6 7.6l2.1-1.6 3.2 2.6-1.4 2.6c-7.4 0-13.7-6.3-13.7-13.7z" fill="none" stroke="#02898f" stroke-width="1.8" stroke-linejoin="round"/>
          <path d="M14 4a6 6 0 0 1 6 6M14 7.5a2.5 2.5 0 0 1 2.5 2.5" fill="none" stroke="#02898f" stroke-width="1.6" stroke-linecap="round"/>
        </svg>
        <span>000-000-0000</span>
      </li>
      <li class="contact-item">
        <svg class="contact-icon" viewBox="0 0 24 24" aria-hidden="true">
          <rect x="3" y="5.5" width="18" height="13" rx="1.5" fill="none" stroke="#02898f" stroke-width="1.8"/>
          <path d="M3.5 6.5l8.5 7 8.5-7" fill="none" stroke="#02898f" stroke-width="1.8" stroke-linejoin="round"/>
        </svg>
        <span>wwwyourmail@.com</span>
      </li>
    </ul>
    <div class="accent-bar-bottom"></div>
    <p class="brand-name">AEROLIS</p>
  </section>

  <section class="card card-back" aria-label="Business card back">
    <div class="turbine-pattern" role="img" aria-label="Subtle tone-on-tone repeating pattern of wind turbines"></div>
    <div class="qr-placeholder">QR</div>
  </section>
</main>
</body>
</html>
```